Corvane Collective Web Presence Design and Relaunch

Take existing web files and "clean up" for a a more presentable web landing pad.
posted presently on a site pad CSS template. at www.corvanecollective.org

The site is clunky and unprofessional looking. Needs to be toned down so the urgency is conveyed, but not via a burning planet image.

Target Market(s)

Non-profit climate adaptation group targeting local government land management agencies, special districts and private landholders of natural resource properties.

Industry/Entity Type

Environment

Coding

Coded - Design and coding required

Number of Pages Required

4 page

Font styles to use
Serif
Sans Serif

Requirements
Must have
• Include current logos, aspects if content on current site www.corvanecollective.org
• A regional Pacific Northwest Focus (US & Canada). Content speaking to urgency but respectful of cultural diversity and norms. Sustainability themes. Emphasis on action and implementation.
Nice to have
• link to like minded projects. Appear to future generations. Diversity in thematic areas ecological resiliency, energy, food security and infrastructure.

```html
<!DOCTYPE html>
<html lang="en">
<head>
<meta charset="utf-8">
<title>Corvane Collective</title>
<link rel="stylesheet" href="https://fonts.googleapis.com/css2?family=Nunito+Sans:wght@300;400;600;700;800&display=swap">
<style>
  :root {
    --white: #ffffff;
    --sky: #6b7d9f;
    --sky-light: #9aa9c4;
    --smoke: #3b3d46;
    --smoke-deep: #2a2b31;
    --ridge: #4a5566;
    --foliage: #1c2619;
    --shade: rgba(10, 14, 22, 0.35);
  }
  * { box-sizing: border-box; margin: 0; padding: 0; }
  html, body { width: 1200px; height: 744px; overflow: hidden; }
  body { font-family: "Nunito Sans", Arial, sans-serif; color: var(--white); background: var(--smoke-deep); }

  .hero { position: relative; width: 1200px; height: 744px; overflow: hidden; }

  .hero-photo {
    position: absolute; inset: 0;
    background:
      radial-gradient(ellipse 360px 330px at 520px 330px, var(--smoke) 0%, rgba(59,61,70,0.85) 45%, rgba(59,61,70,0) 100%),
      radial-gradient(ellipse 160px 140px at 800px 200px, rgba(70,72,82,0.9) 0%, rgba(70,72,82,0) 100%),
      linear-gradient(180deg, rgba(28,38,25,0) 78%, var(--foliage) 92%),
      linear-gradient(180deg, var(--sky) 0%, var(--sky-light) 40%, var(--ridge) 70%, var(--foliage) 100%);
  }
  .hero-photo::after { content: ""; position: absolute; inset: 0; background: var(--shade); }

  .brand {
    position: absolute; left: 29px; top: 31px;
    display: flex; align-items: center; gap: 10px;
  }
  .brand-mark { width: 40px; height: 40px; border: 2px solid var(--white); border-radius: 50%; }
  .brand-name {
    font-weight: 300; font-size: 20px; line-height: 17px; letter-spacing: 0.2px;
    text-transform: uppercase;
  }

  .headline {
    position: absolute; left: 0; right: 0; top: 250px;
    text-align: center; font-weight: 700; font-size: 42px; line-height: 58px;
    letter-spacing: -0.3px;
  }

  .cta {
    position: absolute; left: 533px; top: 469px; width: 134px; height: 41px;
    border: 3px solid var(--white); border-radius: 2px;
    display: flex; align-items: center; justify-content: center;
    font-weight: 600; font-size: 16px; color: var(--white); text-decoration: none;
  }

  .section-nav { position: absolute; right: 44px; top: 272px; list-style: none; }
  .section-nav li {
    height: 45px; display: flex; align-items: flex-start; justify-content: flex-end; gap: 12px;
  }
  .section-nav .label { font-size: 13px; font-weight: 400; line-height: 20px; }
  .section-nav .dot { width: 12px; height: 12px; margin-top: 4px; border-radius: 50%; background: var(--white); }
  .section-nav .active .dot { width: 15px; height: 15px; margin-top: 3px; margin-right: -1px; background: none; border: 1.5px solid var(--white); }

  .scroll-cue { position: absolute; left: 585px; top: 680px; }
</style>
</head>
<body>
<main class="hero">
  <div class="hero-photo" role="img" aria-label="Photograph of a volcano sending up a towering dark ash cloud under a blue-grey sky, with trees and power lines in the foreground"></div>

  <header class="brand">
    <span class="brand-mark"></span>
    <span class="brand-name">Corvane<br>Collective</span>
  </header>

  <h1 class="headline">We are implementing climate strategies<br>throughout the Pacific Northwest<br>for generations to come</h1>

  <a class="cta" href="#">Join Us</a>

  <ul class="section-nav">
    <li class="active"><span class="label">Home</span><span class="dot"></span></li>
    <li><span class="dot"></span></li>
    <li><span class="dot"></span></li>
    <li><span class="dot"></span></li>
    <li><span class="dot"></span></li>
  </ul>

  <svg class="scroll-cue" width="31" height="53" viewBox="0 0 31 53" aria-hidden="true">
    <rect x="1.5" y="1.5" width="28" height="50" rx="14" fill="none" stroke="#ffffff" stroke-width="2"/>
    <circle cx="15.5" cy="36" r="2.5" fill="#ffffff"/>
  </svg>
</main>
</body>
</html>
```